Agency Growth Partnership Graphic Layout

We need to create a graphic depiction of how our agency helps other advertising agencies make money from the project we start with - and they add on to with elements like PR, ads, and other marketing services that are detailed in the pdf document. The goal is for them to see how the Hollywood project we create is an idea they want to help sell in the clients. The two images we have now are not sexy enough. Originally the idea was to show a seed planted that grows to allow everyone to benefit from the plant. The plant would be the celebrity or TV or Film partnership we create, and then that grows healthier and becomes more robust. However, after we went originally down the path of a plant, we realized it wasn't very sexy looking, and the image our internal team made is not very graphically pleasing or high end enough. We need the graphic to feel like Hollywood, be cool, professional and be attention getting. The graphic can take up an entire PowerPoint page. The second image shows how the other agencies all work with one another (like cogs) off of the central idea that Marquee Crafted creates. I like the ideas of growth and plants - but open to other ideas that will show this depiction

Target Market(s)

Media agency executives

Industry/Entity Type

Ad Agency

Font styles to use
Sans Serif

Requirements
Must have
• Everything included (words) in the attached document.
• Our colors are #9b0230 as well as greys, white and black.
Nice to have
• Images that show how the concepts are building blocks, growth, working together
Should not have
• Cartoonish.

```html
<!DOCTYPE html>
<html lang="en">
<head>
<meta charset="UTF-8">
<title>360º Activation</title>
<link rel="stylesheet" href="https://fonts.googleapis.com/css2?family=Jost:wght@500;600;700&display=swap">
<style>
  :root {
    --brand-red: #9b0230;
    --block-red: #a3143d;
    --ring-red: #7a1a2e;
    --node-brown: #6b1c1f;
    --halo-pink: #b77a88;
    --core-red: #8a1c34;
    --leaf-green: #c3c96a;
    --leaf-dark: #2f4a45;
    --ink: #111111;
    --paper: #ffffff;
  }
  * { margin: 0; padding: 0; box-sizing: border-box; }
  html, body { width: 1200px; height: 674px; overflow: hidden; background: var(--paper); }
  .slide {
    position: relative;
    width: 1200px;
    height: 674px;
    overflow: hidden;
    background: var(--paper);
    font-family: "Jost", "Futura", sans-serif;
    color: var(--ink);
  }
  .slide-title {
    position: absolute;
    left: 38px;
    top: 56px;
    font-size: 31px;
    font-weight: 700;
    letter-spacing: 0.3px;
  }
  .growth-illustration {
    position: absolute;
    left: 22px;
    top: 144px;
    width: 282px;
    height: 212px;
    background: radial-gradient(ellipse at 50% 45%, var(--leaf-green) 0%, #a9b25a 45%, rgba(255,255,255,0) 72%);
  }
  .brand-block {
    position: absolute;
    left: 0;
    top: 318px;
    width: 350px;
    height: 356px;
    background: var(--block-red);
  }
  .powered-by {
    position: absolute;
    left: 0;
    width: 350px;
    top: 554px;
    text-align: center;
    color: var(--paper);
    font-size: 28px;
    font-weight: 500;
    line-height: 29px;
  }
  .activation-diagram {
    position: absolute;
    left: 0;
    top: 0;
  }
  .core-label {
    position: absolute;
    left: 683px;
    top: 320px;
    width: 180px;
    text-align: center;
    color: var(--paper);
    font-size: 20px;
    font-weight: 600;
    line-height: 20px;
  }
  .channel {
    position: absolute;
    font-size: 15px;
    font-weight: 600;
    line-height: 16px;
    white-space: nowrap;
  }
  .channel.right-side { text-align: left; }
  .channel.left-side { text-align: right; transform: translateX(-100%); }
  .channel.centered { text-align: center; transform: translateX(-50%); }
</style>
</head>
<body>
<main class="slide">
  <h1 class="slide-title">360º ACTIVATION</h1>

  <div class="growth-illustration" role="img" aria-label="Illustration of a young tree with leafy branches rising from the ground"></div>

  <section class="brand-block">
  </section>
  <p class="powered-by">powered by<br>Marquee Crafted</p>

  <svg class="activation-diagram" width="1200" height="674" viewBox="0 0 1200 674" aria-hidden="true">
    <circle cx="773" cy="342" r="223" fill="none" stroke="var(--ring-red)" stroke-width="2"/>
    <circle cx="773" cy="346" r="178" fill="var(--halo-pink)"/>
    <circle cx="773" cy="346" r="88" fill="var(--core-red)"/>
    <g fill="var(--paper)" stroke="var(--node-brown)" stroke-width="7">
      <circle cx="773" cy="118" r="13"/>
      <circle cx="868" cy="140" r="13"/>
      <circle cx="942" cy="193" r="13"/>
      <circle cx="990" cy="285" r="13"/>
      <circle cx="990" cy="398" r="13"/>
      <circle cx="942" cy="492" r="13"/>
      <circle cx="868" cy="544" r="13"/>
      <circle cx="773" cy="565" r="13"/>
      <circle cx="674" cy="544" r="13"/>
      <circle cx="604" cy="490" r="13"/>
      <circle cx="556" cy="394" r="13"/>
      <circle cx="556" cy="285" r="13"/>
      <circle cx="604" cy="193" r="13"/>
      <circle cx="674" cy="140" r="13"/>
    </g>
  </svg>

  <p class="core-label">360º<br>ACTIVATION</p>

  <p class="channel centered" style="left:782px; top:63px;">Influencer Ad On<br>(Micro, macro, Blogger)</p>
  <p class="channel right-side" style="left:917px; top:110px;">Game Show<br>Add On</p>
  <p class="channel right-side" style="left:969px; top:166px;">Talk Show<br>Add On</p>
  <p class="channel right-side" style="left:1020px; top:262px;">News Segment<br>Add On</p>
  <p class="channel right-side" style="left:1020px; top:379px;">Magazine<br>Advetorial</p>
  <p class="channel right-side" style="left:982px; top:492px;">Coupons</p>
  <p class="channel right-side" style="left:905px; top:558px;">Sweeptstakes<br>&amp; Contests</p>
  <p class="channel centered" style="left:779px; top:597px;">Event Activation</p>
  <p class="channel left-side" style="left:652px; top:560px;">Digital Content for Ads<br>(Digital Ads)</p>
  <p class="channel left-side" style="left:570px; top:490px;">FSI</p>
  <p class="channel left-side" style="left:521px; top:391px;">Email</p>
  <p class="channel left-side" style="left:525px; top:274px;">Social<br>Content</p>
  <p class="channel left-side" style="left:571px; top:182px;">Whitelisted<br>Posts</p>
  <p class="channel left-side" style="left:637px; top:121px;">Experiential<br>Extensions</p>
</main>
</body>
</html>
```